Brantley Advisory Group provides support for renewable energy projects to utilities and suppliers

I need a professional looking business card that is both simple and elegant and unique. My clients are mostly large organizations not individuals. I am a consultant with my own company that is small but would like to give clients the impression I am larger. Smart grid, fiber optics, software, field hardware, distribution automation, substation automation, operations, energy storage/batteries, microgrids, customer service, strategy/roadmaps, conservation, Automated Metering Infrastruture (AMI or smart meters) are all areas of focus.

Target Market(s)

Utilities, suppliers, governmental agencies involved in energy. All types of energy especially natural gas and electrical. Especially renewable energy or green projects.

Contact Information for Business Card

Name - Ross Brantley Cell Phone - 425.318.4762 Email - rbrantley@brantleyag-example.com
Company - Brantley Advisory Group (logo) Title - Principal

Font styles to use
Serif
Sans Serif

Colors

Designer to choose colors to be used in the design.

Requirements
Must have
• Simple and professional and powerful.
• Unique/creative design.
Nice to have
• Utilize color scheme to accent logo colors. Maybe some geometric pattern on edge of card with color.
Should not have
• Busy, complicated, traditional

```html
<!DOCTYPE html>
<html lang="en">
<head>
<meta charset="utf-8">
<title>Brantley Advisory Group – Business Card</title>
<link rel="stylesheet" href="https://fonts.googleapis.com/css2?family=Arimo:wght@400;700&display=swap">
<style>
  :root {
    --brand-blue: #1f3f99;
    --brand-green: #5e8c3a;
    --accent-gray: #a3a3a3;
    --card-white: #ffffff;
    --page-bg: #e6e7ea;
    --ink-white: #ffffff;
  }
  html, body {
    margin: 0;
    padding: 0;
    width: 1200px;
    height: 960px;
    overflow: hidden;
    background: var(--page-bg);
    font-family: "Arimo", Arial, sans-serif;
  }
  .sheet {
    width: 1200px;
    height: 960px;
    display: flex;
    flex-direction: column;
    align-items: center;
    justify-content: center;
    gap: 56px;
  }
  .card {
    position: relative;
    width: 700px;
    height: 400px;
    overflow: hidden;
    box-shadow: 0 6px 18px rgba(0,0,0,0.18);
  }
  /* Back of card */
  .card-back {
    background: var(--brand-blue);
  }
  .card-back .texture {
    position: absolute;
    inset: 0;
    background: radial-gradient(circle at 50% 45%, #2648a6 0%, var(--brand-blue) 70%);
  }
  .card-back .wordmark {
    position: absolute;
    left: 0; right: 0; top: 0; bottom: 0;
    display: flex;
    align-items: center;
    justify-content: center;
    gap: 18px;
    color: var(--ink-white);
    font-weight: 700;
    font-size: 40px;
    letter-spacing: 0.5px;
  }
  .wordmark .mark-square {
    width: 34px;
    height: 34px;
    border: 4px solid currentColor;
    border-radius: 6px;
    box-sizing: border-box;
  }
  /* Front of card */
  .card-front {
    background: var(--card-white);
  }
  .card-front .shapes {
    position: absolute;
    inset: 0;
  }
  .card-front .wordmark {
    position: absolute;
    left: 40px;
    top: 40px;
    display: flex;
    align-items: center;
    gap: 12px;
    color: var(--brand-blue);
    font-weight: 700;
    font-size: 26px;
  }
  .card-front .wordmark .mark-square {
    width: 26px;
    height: 26px;
    border-width: 3px;
  }
  .holder {
    position: absolute;
    left: 40px;
    top: 140px;
    color: var(--ink-white);
  }
  .holder-name {
    font-weight: 700;
    font-size: 24px;
    margin: 0;
  }
  .holder-title {
    font-size: 18px;
    margin: 4px 0 0;
  }
  .contact {
    position: absolute;
    right: 36px;
    top: 286px;
    text-align: right;
    color: var(--ink-white);
    font-size: 16px;
    line-height: 22px;
  }
  .contact-line {
    display: flex;
    justify-content: flex-end;
    align-items: center;
    gap: 8px;
    margin: 0;
  }
  .contact-line svg {
    width: 14px;
    height: 14px;
    fill: var(--ink-white);
  }
  .contact-address { margin: 6px 0 0; }
</style>
</head>
<body>
<main class="sheet">

  <section class="card card-back" aria-label="Card back">
    <div class="texture" role="img" aria-label="Subtle tonal pattern in brand blue"></div>
    <div class="wordmark">
      <span class="mark-square" aria-hidden="true"></span>
      <span>Brantley Advisory Group</span>
    </div>
  </section>

  <section class="card card-front" aria-label="Card front">
    <svg class="shapes" viewBox="0 0 700 400" width="700" height="400" aria-hidden="true">
      <polygon points="0,120 420,120 350,170 300,215 0,215" fill="var(--brand-green)"/>
      <polygon points="175,270 265,238 330,400 175,400" fill="var(--accent-gray)"/>
      <polygon points="255,190 700,255 700,400 340,400" fill="var(--brand-blue)"/>
      <polygon points="0,215 300,215 275,230 0,226" fill="var(--card-white)"/>
    </svg>

    <div class="wordmark">
      <span class="mark-square" aria-hidden="true"></span>
      <span>Brantley Advisory Group</span>
    </div>

    <div class="holder">
      <p class="holder-name">Ross Brantley</p>
      <p class="holder-title">Principal</p>
    </div>

    <div class="contact">
      <p class="contact-line">
        <svg viewBox="0 0 24 24" aria-hidden="true"><path d="M6.6 10.8a15.5 15.5 0 0 0 6.6 6.6l2.2-2.2c.3-.3.7-.4 1-.2 1.1.4 2.3.6 3.6.6.6 0 1 .4 1 1V20c0 .6-.4 1-1 1A17 17 0 0 1 3 4c0-.6.4-1 1-1h3.5c.6 0 1 .4 1 1 0 1.3.2 2.5.6 3.6.1.3 0 .7-.2 1z"/></svg>
        <span>425.318.4762</span>
      </p>
      <p class="contact-line">
        <svg viewBox="0 0 24 24" aria-hidden="true"><path d="M2 5h20v14H2zm2 2v.5l8 5 8-5V7l-8 5z"/></svg>
        <span>rbrantley@brantleyag-example.com</span>
      </p>
      <p class="contact-address">Street Name, City Name<br>Zipcode - 012345</p>
    </div>
  </section>

</main>
</body>
</html>
```